Savour and Thrive Wellbeing is being Launched and needs a business card and stationery package

I need a stationery package including business card (primary focus) , letterhead, digital letterhead, envelopes, with compliments slip, A 5 note sheet for the rebranding of my business and launch of my new website. I have a logo, like beige, brown earthy tones with a hint of red. I would also like the option of my letterhead also being printed on recycled paper in another format as well as the traditional letterhead. I do also send my letters to GPs and specialists digitally as well. I like to stand out from the usual stereotype of fruits and vegetables on business cards as I find that quite tacky and stereotypical. I want the business card to capture the essence of my logo as natural, nutrition, enjoyment, nurturing and freedom with food. I have attached the logo, and additional brief sheet on my ideas. Happy to have any background that is complementary to my theme, and what you believe would be catching. Definitely DONT'T like pink, try to pick up the darker colour in the logo please. and think too much black is a little overpowering.

Target Market(s)

clients who are interested in improving their health and wellness. Client 80% females; 20% males

Industry/Entity Type

Health And Wellness

Contact Information for Business Card

I am open to having different backgrounds as well that would complement the logo. Probably less emphasis on the heart out of the logo - just happy to keep that in the logo only please
I am also wanting two business cards - one for the appointments, one for general distribution and media distribution (both need to look consistent though) - but does give opportunity for one of the business cards to be less wordy and more striking. And the front of the business card can certainly stand out with the entire savour and thrive logo and my name and grab the attention of the receiver.
1st business card
on front:
Lorena Whitcombe
Savour and Thrive Wellbeing & logo
Nutritionist and Dietitian
Tarvel Medical Centre
647 Brindle Hill Rd, Quorrel Q 4987
Phone: (07) 3017 2968 Fax: (07) 3156 7209
Mobile: 0400 261 937
www.savourandthrivewellbeing.example.au
lorena@savourandthrivewellbeing.example.au
on back:
next appointment

……………………….. at ……………………… (possibly 4 times)
If you are unable to keep your appointment, please contact us as soon as possible (small font)
2nd business card (needs to be very eye catching and stand out)
on front: Savour and Thrive Wellbeing logo and my name
on back:
Lorena Whitcombe
address
phones, fax, website, email address

Font styles to use
Other font styles liked:
• please refer to logo

Requirements
Must have
• refreshing and simple; new and vibrant - I am rebranding my business after 20 years
• to get a feel of what is the theme - go to my new website (not completed as yet - but you will get a preliminary view) - don't do as google search as blocked - but can put into website header and it will be shown
• www.savourandthrivewellbeing.example.au - but please ignore the colouring of the 4 blocks under the slider on the home page - I am not wanting these colourings - they are getting updated.
Nice to have
• earthy tones, beige, hint of red, fonts to match logo if possible, organic, modern
• get inspiration from my logo please, open to having other backgrounds that complement
Should not have
• no food shots or stereotypical weight/ scales images
• no green, yellow or orange

```html
<!DOCTYPE html>
<html lang="en">
<head>
<meta charset="utf-8">
<title>Savour and Thrive Wellbeing – Business Card</title>
<link href="https://fonts.googleapis.com/css2?family=Arimo:wght@400&display=swap" rel="stylesheet">
<style>
  :root {
    --stage: #333333;
    --kraft: #dccab3;
    --kraft-deep: #cfb99e;
    --ink: #3a3434;
    --accent: #a33b4a;
    --motif: #b98a7e;
  }
  * { margin: 0; padding: 0; box-sizing: border-box; }
  html, body {
    width: 1200px; height: 1200px; overflow: hidden;
    background: var(--stage);
    font-family: "Arimo", Arial, sans-serif;
    color: var(--ink);
  }
  .card {
    position: absolute; left: 238px; width: 726px; height: 415px;
    background: linear-gradient(160deg, var(--kraft) 0%, var(--kraft-deep) 100%);
    overflow: hidden;
  }
  .card--front { top: 133px; }
  .card--back { top: 631px; }
  .motif { position: absolute; right: 0; bottom: 0; }
  .brand {
    position: absolute; left: 47px; top: 24px; width: 300px;
    text-align: center;
  }
  .brand__dot {
    display: block; width: 30px; height: 30px; border-radius: 50%;
    background: var(--accent); margin: 0 auto 14px;
  }
  .brand__name { font-size: 22px; color: var(--ink); white-space: nowrap; }
  .name-bar {
    position: absolute; left: 0; top: 189px; width: 6px; height: 31px;
    background: var(--accent);
  }
  .person { position: absolute; left: 40px; top: 190px; }
  .person__name { font-size: 22px; letter-spacing: 0.5px; line-height: 1.1; }
  .person__role { font-size: 17px; margin-top: 4px; }
  .address {
    position: absolute; left: 31px; top: 256px;
    font-size: 18px; line-height: 22.5px;
  }
  .address__pin { position: absolute; left: 0; top: 4px; }
  .address__lines { padding-left: 15px; }
  .address__lines span { display: block; }
  .address__lines span + span { padding-left: 15px; margin-left: -0px; }
  .contacts {
    position: absolute; right: 32px; top: 256px;
    font-size: 18px; text-align: right;
  }
  .contacts__row {
    display: flex; justify-content: flex-end; align-items: center;
    gap: 8px; height: 22.5px;
  }
  .contacts__row--gap { margin-top: 15px; }
  .contacts svg { width: 11px; height: 11px; flex: none; }
  .appointments__title {
    position: absolute; top: 36px; left: 0; width: 100%;
    text-align: center; font-size: 17px;
  }
  .appointments__list { position: absolute; left: 62px; top: 112px; width: 600px; }
  .slot {
    display: flex; align-items: flex-end; height: 64px; font-size: 17px;
  }
  .slot:first-child { height: 20px; }
  .slot__dots { flex: 1; border-bottom: 2px dotted var(--ink); height: 1px; margin-bottom: 4px; }
  .slot__at { padding: 0 6px; line-height: 1; }
  .appointments__note {
    position: absolute; top: 366px; left: 0; width: 100%;
    text-align: center; font-size: 15px;
  }
</style>
</head>
<body>

<section class="card card--front">
  <svg class="motif" width="360" height="415" role="img" aria-label="Faint oversized leaf motif in muted rose">
    <defs>
      <radialGradient id="motifFront" cx="80%" cy="75%" r="70%">
        <stop offset="0" stop-color="var(--motif)" stop-opacity="0.45"/>
        <stop offset="1" stop-color="var(--motif)" stop-opacity="0"/>
      </radialGradient>
    </defs>
    <rect width="360" height="415" fill="url(#motifFront)"/>
  </svg>

  <div class="brand">
    <span class="brand__dot"></span>
    <div class="brand__name">Savour and Thrive Wellbeing</div>
  </div>

  <div class="name-bar"></div>
  <div class="person">
    <div class="person__name">LORENA WHITCOMBE</div>
    <div class="person__role">Nutritionist and Dietitian</div>
  </div>

  <div class="address">
    <svg class="address__pin" width="10" height="13" viewBox="0 0 10 13"><path d="M5 0a5 5 0 0 0-5 5c0 3.5 5 8 5 8s5-4.5 5-8a5 5 0 0 0-5-5zm0 7a2 2 0 1 1 0-4 2 2 0 0 1 0 4z" fill="var(--ink)"/></svg>
    <div class="address__lines">
      <span style="padding-left:0">Tarvel Medical Centre</span>
      <span>647 Brindle Hill Rd,</span>
      <span>Quorrel Q 4987</span>
    </div>
  </div>

  <div class="contacts">
    <div class="contacts__row">(07) 3017 2968
      <svg viewBox="0 0 12 12"><path d="M1 4c0-2 2-3 5-3s5 1 5 3H8V3H4v1zM2 5h8l1 6H1z" fill="var(--ink)"/></svg></div>
    <div class="contacts__row">(07) 3156 7209
      <svg viewBox="0 0 12 12"><path d="M3 0h5v4H3zM1 4h10v8H1z" fill="var(--ink)"/></svg></div>
    <div class="contacts__row">0400 261 937
      <svg viewBox="0 0 12 12"><rect x="3" y="0.5" width="6" height="11" rx="1" fill="none" stroke="var(--ink)"/></svg></div>
    <div class="contacts__row contacts__row--gap">www.savourandthrivewellbeing.example.au
      <svg viewBox="0 0 12 12"><circle cx="6" cy="6" r="5" fill="none" stroke="var(--ink)" stroke-width="1.5"/><path d="M1 6h10M6 1c-3 3-3 7 0 10M6 1c3 3 3 7 0 10" fill="none" stroke="var(--ink)"/></svg></div>
    <div class="contacts__row">lorena@savourandthrivewellbeing.example.au
      <svg viewBox="0 0 12 12"><rect x="0.5" y="2.5" width="11" height="7" fill="var(--ink)"/><path d="M0.5 2.5l5.5 4 5.5-4" fill="none" stroke="var(--kraft)"/></svg></div>
  </div>
</section>

<section class="card card--back">
  <svg class="motif" width="460" height="415" role="img" aria-label="Faint oversized leaf motif in muted rose">
    <defs>
      <radialGradient id="motifBack" cx="75%" cy="55%" r="75%">
        <stop offset="0" stop-color="var(--motif)" stop-opacity="0.45"/>
        <stop offset="1" stop-color="var(--motif)" stop-opacity="0"/>
      </radialGradient>
    </defs>
    <rect width="460" height="415" fill="url(#motifBack)"/>
  </svg>

  <div class="appointments__title">Next Appointment</div>
  <div class="appointments__list">
    <div class="slot"><span class="slot__dots"></span><span class="slot__at">at</span><span class="slot__dots"></span></div>
    <div class="slot"><span class="slot__dots"></span><span class="slot__at">at</span><span class="slot__dots"></span></div>
    <div class="slot"><span class="slot__dots"></span><span class="slot__at">at</span><span class="slot__dots"></span></div>
    <div class="slot"><span class="slot__dots"></span><span class="slot__at">at</span><span class="slot__dots"></span></div>
  </div>
  <div class="appointments__note">If you are unable to keep your appointment, please contact us as soon as possible</div>
</section>

</body>
</html>
```